Ridgeway Business Card Redesign

Using the current logo/tagline lock-up and icon, redesign the Ridgeway business card to better show the tagline and improve the layout to give the card a more timely design and a classic, sophisticated look. See attached Project Brief for more detail.

```html
<!DOCTYPE html>
<html lang="en">
<head>
<meta charset="utf-8">
<title>Ridgeway Capital – Business Card</title>
<link rel="stylesheet" href="https://fonts.googleapis.com/css2?family=Source+Serif+4:wght@400;600&display=swap">
<style>
  :root {
    --backdrop: #e4e1dc;
    --card: #ffffff;
    --blue: #1a72bb;
    --ink: #3a3a3c;
    --charcoal: #404042;
    --rule: #555557;
  }
  * { box-sizing: border-box; margin: 0; padding: 0; }
  html, body { width: 900px; height: 1200px; overflow: hidden; }
  body {
    background: var(--backdrop);
    font-family: "Source Serif 4", Georgia, serif;
    color: var(--ink);
    position: relative;
  }
  .card {
    position: absolute;
    left: 86px;
    width: 736px;
    height: 428px;
    background: var(--card);
    box-shadow: 0 6px 14px rgba(0,0,0,0.25);
  }
  .card--top { top: 137px; }
  .card--bottom { top: 634px; }

  .brand-mark {
    position: absolute;
    left: 30px; top: 40px;
    width: 84px; height: 84px;
    border-radius: 50%;
    background: var(--blue);
  }
  .brand-name {
    position: absolute;
    left: 140px; top: 56px;
    font-size: 40px;
    font-weight: 400;
    line-height: 1.2;
    color: var(--charcoal);
  }
  .tagline {
    position: absolute;
    left: 141px; top: 138px;
    font-size: 17px;
    color: var(--blue);
  }

  .holder {
    position: absolute;
    right: 22px; top: 191px;
    text-align: right;
  }
  .holder__name { font-size: 25.5px; font-weight: 600; color: var(--blue); line-height: 32px; }
  .holder__title { font-size: 23px; line-height: 31px; }
  .divider {
    position: absolute;
    left: 0; top: 239px;
    width: 322px; height: 2px;
    background: var(--rule);
  }

  .address {
    position: absolute;
    left: 24px; top: 309px;
    font-size: 20px;
    line-height: 27px;
  }
  .address__web { color: var(--blue); font-size: 22px; line-height: 30px; }

  .contacts {
    position: absolute;
    right: 22px; top: 287px;
    text-align: right;
    font-size: 19.5px;
    line-height: 26px;
  }
  .contacts dt { display: inline; color: var(--blue); font-weight: 600; }
  .contacts dd { display: inline; }
  .contacts dd::after { content: "\A"; white-space: pre; }

  .band { position: absolute; left: 0; bottom: 0; width: 736px; height: 25px; }
</style>
</head>
<body>
  <article class="card card--top">
    <div class="brand-mark"></div>
    <div class="brand-name">Ridgeway Capital</div>
    <div class="tagline">Non-Control Growth Capital</div>
    <div class="divider"></div>
    <div class="holder">
      <div class="holder__name">Daniel R. Ashford</div>
      <div class="holder__title">Principal &amp; Chief Marketing Officer</div>
    </div>
    <div class="address">
      41 Harbor Mill Road<br>
      Suite 210, Milford, CT 06460<br>
      <span class="address__web">www.ridgewaycapital.com</span>
    </div>
    <dl class="contacts">
      <dt>Direct:</dt> <dd>(555) 014-2210</dd>
      <dt>Office:</dt> <dd>(555) 018-4471</dd>
      <dt>Cell:</dt> <dd>(555) 016-3382</dd>
      <dd>dashford@ridgewaycapital.com</dd>
    </dl>
    <svg class="band" viewBox="0 0 736 25" aria-hidden="true">
      <polygon points="0,0 356,0 345,25 0,25" fill="var(--charcoal)"/>
      <polygon points="364,0 736,0 736,25 353,25" fill="var(--blue)"/>
    </svg>
  </article>

  <article class="card card--bottom">
    <div class="brand-mark"></div>
    <div class="brand-name">Ridgeway Capital</div>
    <div class="tagline">Non-Control Growth Capital</div>
    <div class="divider"></div>
    <div class="holder">
      <div class="holder__name">Daniel R. Ashford</div>
      <div class="holder__title">Principal &amp; Chief Marketing Officer</div>
    </div>
    <div class="address">
      41 Harbor Mill Road<br>
      Suite 210, Milford, CT 06460<br>
      <span class="address__web">www.ridgewaycapital.com</span>
    </div>
    <dl class="contacts">
      <dt>Direct:</dt> <dd>(555) 014-2210</dd>
      <dt>Office:</dt> <dd>(555) 018-4471</dd>
      <dt>Cell:</dt> <dd>(555) 016-3382</dd>
      <dd>dashford@ridgewaycapital.com</dd>
    </dl>
    <svg class="band" viewBox="0 0 736 25" aria-hidden="true">
      <polygon points="0,0 356,0 345,25 0,25" fill="var(--charcoal)"/>
      <polygon points="364,0 736,0 736,25 353,25" fill="var(--blue)"/>
    </svg>
  </article>
</body>
</html>
```